Redesign Current Opencart Site - More Calls to actions

Our current site is www.tallowcrestdesk.co.uk, we had it built around 18 months ago(poorly) and the site was handed over unfinished.
We had to learn basics and pay other people to get it to the useable state it is and have been using it since. We started building www.quillbarrowstonecraftdepot.com and prefer the layout of opencart.

We want to stick with opencart as the backend, but want several pages redesigning to give a better company image and also have more CTA's across the site.

Once quillbarrowstonecraftdepot is complete, we will swap the site across to replace the tallowcrestdesk site. Hope that makes sense.

We want the following pages redesigned:

Homepage/corporate repairs/FAQ's/Howitworks/Reviews/Contact us

we work with a lot of corporate clients but want to push our retail arm whilst still giving a strong positive image about us and our services.

We need more CTA's making people purchase from our site.
Thanks
Dorin
Updates

Would like to portray a more corporate image Thanks

Target Market(s)

21-44 year olds

Coding

Coded - Design and coding required

Number of Pages Required

5+ page

Other font styles liked:
• current font on banners is harabara

Colors
0592cd
acd036

Requirements
Must have
• more CTA's
• benefits of why to use our services
• Keep fonts and colours the same as above sites.

```html
<!DOCTYPE html>
<html lang="en">
<head>
<meta charset="utf-8">
<title>Tallowcrest Desk – Same Day Phone &amp; Tablet Repairs</title>
<link href="https://fonts.googleapis.com/css2?family=Open+Sans:wght@400;600;700;800&family=Ubuntu:wght@500;700&display=swap" rel="stylesheet">
<style>
:root{
  --blue:#0592cd;
  --blue-dark:#047aab;
  --green:#acd036;
  --green-dark:#94b82a;
  --ink:#3b3b3b;
  --muted:#8a8a8a;
  --line:#e3e3e3;
  --pale:#f3f3f3;
  --footer:#3d3d3d;
  --footer-deep:#2e2e2e;
  --white:#fff;
}
*{box-sizing:border-box;margin:0;padding:0}
html,body{width:1200px;height:3200px;overflow:hidden}
body{font-family:"Open Sans",Arial,sans-serif;color:var(--ink);background:var(--white);font-size:13px;line-height:1.5}
.wrap{width:1040px;margin:0 auto;position:relative}
svg{display:block}

/* header */
.site-header{height:150px;display:flex;align-items:center}
.site-header .wrap{display:flex;align-items:center;justify-content:space-between}
.brand{display:flex;align-items:center;gap:12px}
.brand-dot{width:22px;height:22px;border-radius:50%;background:var(--green)}
.brand-name{font-family:"Ubuntu",sans-serif;font-weight:700;font-size:34px;color:var(--blue);line-height:1}
.brand-tag{font-size:11px;color:var(--muted);margin-top:4px}
.header-info{display:flex;gap:44px}
.info-block{display:flex;align-items:center;gap:10px;padding-left:22px;border-left:1px solid var(--line)}
.info-block:first-child{border-left:0}
.info-label{font-size:11px;color:var(--muted)}
.info-value{font-size:15px;font-weight:700;color:var(--blue)}
.stars{display:flex;gap:2px;margin-top:3px}

/* nav */
.main-nav{background:var(--blue);height:40px}
.main-nav ul{list-style:none;display:flex;width:1040px;margin:0 auto;height:40px}
.main-nav li{flex:1;text-align:center;color:var(--white);font-size:12px;font-weight:600;line-height:40px;text-transform:uppercase}
.main-nav li.active{background:var(--green)}

/* why us */
.why-us{background:var(--pale);height:160px;padding-top:22px}
.section-title{font-size:24px;font-weight:700;color:var(--ink);text-align:center}
.why-list{display:flex;justify-content:space-between;margin-top:28px}
.why-item{display:flex;align-items:center;gap:10px;font-size:11px;font-weight:600;color:var(--muted);text-transform:uppercase}
.why-icon{width:30px;height:30px;border-radius:50%;background:var(--green);display:flex;align-items:center;justify-content:center}

/* hero */
.hero{height:580px;position:relative;background:linear-gradient(100deg,#3c4249 0%,#5d646b 38%,#b9bcbf 70%,#dcdedf 100%)}
.hero-overlay{position:absolute;inset:0;background:linear-gradient(90deg,rgba(30,34,38,.75) 0%,rgba(30,34,38,.35) 45%,rgba(0,0,0,0) 70%)}
.hero-copy{position:absolute;left:120px;top:130px;width:470px}
.hero-kicker{font-family:"Ubuntu",sans-serif;font-weight:500;font-size:30px;color:var(--green);line-height:1.2}
.hero-title{font-family:"Ubuntu",sans-serif;font-weight:700;font-size:52px;color:var(--white);line-height:1.15;margin-top:10px}
.hero-text{color:#e6e6e6;font-size:12px;margin-top:14px}
.hero-actions{display:flex;gap:14px;margin-top:28px}
.btn{display:inline-block;padding:10px 22px;font-size:11px;font-weight:700;color:var(--white);text-transform:uppercase;border-radius:2px}
.btn-blue{background:var(--blue)}
.btn-green{background:var(--green)}
.slide-arrow{position:absolute;top:260px;width:40px;height:60px;background:rgba(255,255,255,.25);display:flex;align-items:center;justify-content:center}
.slide-arrow.prev{left:0}.slide-arrow.next{right:0}

/* instore strip */
.instore-strip{height:60px;border-bottom:1px solid var(--line)}
.instore-strip .wrap{display:flex;align-items:center;height:60px;gap:24px}
.strip-title{font-family:"Ubuntu",sans-serif;font-size:20px;font-weight:700;color:var(--blue)}
.strip-text{font-size:10px;color:var(--muted)}
.strip-phone{display:flex;align-items:center;gap:6px;font-weight:700;font-size:16px;color:var(--green)}

/* featured */
.featured{height:390px;padding-top:46px}
.featured-head{display:flex;justify-content:space-between;align-items:center}
.featured-head h2{font-size:26px;font-weight:700}
.arrows{display:flex;gap:6px}
.arrow-btn{width:26px;height:26px;border-radius:50%;background:var(--line);display:flex;align-items:center;justify-content:center}
.product-row{display:flex;justify-content:space-between;margin-top:26px}
.product{width:190px;text-align:center;border-right:1px solid var(--line)}
.product:last-child{border-right:0}
.product-photo{width:110px;height:150px;margin:0 auto;background:linear-gradient(160deg,#2b2b2b,#5a5a5a);border-radius:10px}
.product-name{font-size:13px;color:var(--ink);margin-top:18px}
.product-buy{display:flex;justify-content:center;gap:10px;margin-top:12px}
.price{background:var(--green);color:var(--white);font-size:12px;font-weight:700;padding:4px 12px}
.cart-btn{background:var(--blue);width:28px;height:26px;display:flex;align-items:center;justify-content:center}

/* steps */
.steps{height:520px;background:linear-gradient(135deg,#0592cd 0%,#0a7fb4 50%,#0592cd 100%);padding-top:42px}
.steps h2{color:var(--white);font-size:24px;font-weight:700;text-align:center}
.step-row{display:flex;justify-content:space-between;margin-top:36px;padding:0 40px}
.step-card{width:220px;background:var(--white);text-align:center;padding-bottom:0}
.step-head{background:var(--green);color:var(--white);font-weight:700;font-size:15px;text-transform:uppercase;padding:18px 0 58px}
.step-icon{width:80px;height:80px;border-radius:50%;background:var(--white);border:4px solid var(--blue);margin:-44px auto 0;display:flex;align-items:center;justify-content:center}
.step-num{color:var(--blue);font-weight:700;font-size:15px;margin-top:14px}
.step-text{font-size:10px;color:var(--muted);padding:6px 18px 16px}
.step-more{background:#555;color:var(--white);font-size:11px;font-weight:600;padding:8px 0}

/* benefits */
.benefits{height:380px;padding-top:50px}
.benefits .wrap{display:flex;justify-content:space-between}
.col{width:490px}
.col h3{font-size:20px;font-weight:700;margin-bottom:22px}
.benefit{display:flex;gap:14px;margin-bottom:18px}
.diamond{width:12px;height:12px;background:var(--green);transform:rotate(45deg);margin-top:5px;flex:none}
.benefit-title{color:var(--blue);font-weight:700;font-size:14px}
.benefit-text{font-size:11px;color:var(--muted)}
.instore-media{display:flex;gap:20px}
.instore-photo{width:230px;height:140px;background:linear-gradient(135deg,#6b6f74,#c8ccd0);flex:none}
.small-text{font-size:11px;color:var(--muted)}

/* testimonial */
.testimonial{height:260px;background:linear-gradient(90deg,#2d3135,#4a5057 50%,#2d3135);margin-top:20px;position:relative}
.testimonial .wrap{display:flex;align-items:center;gap:50px;height:220px;padding:0 60px}
.avatar{width:130px;height:130px;border-radius:50%;background:linear-gradient(160deg,#b7a58f,#6f655a);border:4px solid var(--white);flex:none}
.quote-mark{font-size:60px;color:var(--white);font-weight:800;line-height:1}
.quote-text{color:#e6e6e6;font-size:12px;font-style:italic}
.dots{display:flex;gap:8px;justify-content:center}
.dots span{width:8px;height:8px;border-radius:50%;background:#888}
.dots span.on{background:var(--white)}

/* cta bar */
.cta-bar{height:80px;border-bottom:1px solid var(--line)}
.cta-bar .wrap{display:flex;align-items:center;justify-content:space-between;height:80px}
.cta-phone{display:flex;align-items:center;gap:10px;font-weight:700;font-size:18px}
.cta-main{display:flex;align-items:center;gap:14px;color:var(--blue);font-weight:700;font-size:18px}
.socials{display:flex;gap:8px}
.socials span{width:28px;height:28px;border-radius:50%;background:#c9c9c9}

/* partners */
.partners{height:210px;background:var(--pale);margin-top:20px}
.partners .wrap{display:flex;align-items:center;justify-content:space-between;height:210px}
.partner{width:112px;height:64px;background:var(--white);border:1px solid var(--line);display:flex;align-items:center;justify-content:center}
.partner span{width:64px;height:20px;background:#d3d3d3;border-radius:3px}

/* footer */
.site-footer{background:var(--footer);height:310px;color:#cfcfcf;padding-top:40px}
.site-footer .wrap{display:flex;justify-content:space-between}
.f-col{width:230px}
.f-col h4{color:var(--white);font-size:15px;font-weight:600;margin-bottom:18px}
.field{background:var(--white);height:28px;margin-bottom:10px;color:#999;font-size:11px;padding:6px 10px}
.btn-submit{background:var(--green);color:var(--white);font-size:11px;font-weight:700;padding:7px 18px;display:inline-block}
.f-text{font-size:11px;line-height:1.7}
.f-socials{display:flex;gap:8px;margin-top:14px}
.f-socials span{width:26px;height:26px;border-radius:50%;border:1px solid #8a8a8a}
.f-list{list-style:none;font-size:11px;line-height:2.1}
.f-list li::before{content:"› ";color:var(--green)}
.copyright{background:var(--footer-deep);height:40px;color:#9a9a9a;font-size:10px;text-align:center;line-height:40px}
</style>
</head>
<body>

<header class="site-header">
  <div class="wrap">
    <div class="brand">
      <div class="brand-dot"></div>
      <div>
        <div class="brand-name">Tallowcrest Desk</div>
        <div class="brand-tag">All your device repairs, one trusted place</div>
      </div>
    </div>
    <div class="header-info">
      <div class="info-block">
        <div>
          <div class="info-label">Don't Just Read Reviews</div>
          <div class="stars">
            <svg width="80" height="14" viewBox="0 0 80 14"><g fill="#f5b50a">
              <path d="M7 0l2 4.5 5 .5-3.7 3.3 1 4.8L7 10.7 2.7 13.1l1-4.8L0 5l5-.5z"/>
              <path transform="translate(16)" d="M7 0l2 4.5 5 .5-3.7 3.3 1 4.8L7 10.7 2.7 13.1l1-4.8L0 5l5-.5z"/>
              <path transform="translate(32)" d="M7 0l2 4.5 5 .5-3.7 3.3 1 4.8L7 10.7 2.7 13.1l1-4.8L0 5l5-.5z"/>
              <path transform="translate(48)" d="M7 0l2 4.5 5 .5-3.7 3.3 1 4.8L7 10.7 2.7 13.1l1-4.8L0 5l5-.5z"/>
              <path transform="translate(64)" d="M7 0l2 4.5 5 .5-3.7 3.3 1 4.8L7 10.7 2.7 13.1l1-4.8L0 5l5-.5z"/></g></svg>
          </div>
        </div>
      </div>
      <div class="info-block">
        <svg width="26" height="26" viewBox="0 0 24 24"><rect x="6" y="2" width="12" height="20" rx="2" fill="none" stroke="#0592cd" stroke-width="2"/><circle cx="12" cy="18" r="1.2" fill="#0592cd"/></svg>
        <div><div class="info-label">Call Us On</div><div class="info-value">01632 960418</div></div>
      </div>
      <div class="info-block">
        <svg width="26" height="26" viewBox="0 0 24 24"><path d="M5 8h14l-1.5 13h-11z" fill="none" stroke="#acd036" stroke-width="2"/><path d="M9 8V6a3 3 0 016 0v2" fill="none" stroke="#acd036" stroke-width="2"/></svg>
        <div><div class="info-label">Shopping</div><div class="info-value" style="color:var(--green)">Cart 0 items</div></div>
      </div>
    </div>
  </div>
</header>

<nav class="main-nav">
  <ul>
    <li class="active">Home</li>
    <li>Corporate Repairs</li>
    <li>FAQs</li>
    <li>How It Works</li>
    <li>Reviews</li>
    <li>Contact Us</li>
  </ul>
</nav>

<section class="why-us">
  <div class="wrap">
    <h2 class="section-title">Why Us !!</h2>
    <div class="why-list">
      <div class="why-item"><span class="why-icon"><svg width="14" height="14" viewBox="0 0 14 14"><path d="M2 7l3 3 7-7" stroke="#fff" stroke-width="2" fill="none"/></svg></span>Business Repair Experts</div>
      <div class="why-item"><span class="why-icon"><svg width="14" height="14" viewBox="0 0 14 14"><path d="M2 7l3 3 7-7" stroke="#fff" stroke-width="2" fill="none"/></svg></span>Free Return Delivery</div>
      <div class="why-item"><span class="why-icon"><svg width="14" height="14" viewBox="0 0 14 14"><path d="M2 7l3 3 7-7" stroke="#fff" stroke-width="2" fill="none"/></svg></span>Same Day Instore Repairs</div>
      <div class="why-item"><span class="why-icon"><svg width="14" height="14" viewBox="0 0 14 14"><path d="M2 7l3 3 7-7" stroke="#fff" stroke-width="2" fill="none"/></svg></span>Excellent Customer Care</div>
    </div>
  </div>
</section>

<section class="hero" role="img" aria-label="Photo of a smartphone with a cracked screen and earphones on a desk">
  <div class="hero-overlay"></div>
  <div class="hero-copy">
    <div class="hero-kicker">Same Day Phone &amp; Tablet Repairs<br>Fast FreePost Service</div>
    <div class="hero-title">Book Your Repair Now!</div>
    <p class="hero-text">Send us your broken phone or tablet using our free postal service and we will repair it the same day it arrives. Every repair is tested by our team and returned to you quickly with a full warranty included as standard.</p>
    <div class="hero-actions"><span class="btn btn-blue">Buy Repair</span><span class="btn btn-green">Learn More</span></div>
  </div>
  <div class="slide-arrow prev"><svg width="14" height="24" viewBox="0 0 14 24"><path d="M12 2L2 12l10 10" stroke="#fff" stroke-width="3" fill="none"/></svg></div>
  <div class="slide-arrow next"><svg width="14" height="24" viewBox="0 0 14 24"><path d="M2 2l10 10-10 10" stroke="#fff" stroke-width="3" fill="none"/></svg></div>
</section>

<section class="instore-strip">
  <div class="wrap">
    <div class="strip-title">Same Day Repairs Instore</div>
    <div class="strip-text">Unit 12, Fernbrook Retail Park, Harrowmere HM4 2QT</div>
    <div class="strip-phone"><svg width="16" height="16" viewBox="0 0 24 24"><path d="M6 2l4 4-2 3c1 3 4 6 7 7l3-2 4 4-3 4C10 22 2 14 2 5z" fill="#acd036"/></svg>01632 960418</div>
    <div class="strip-text">Unit 4, Castlegate Walk, Harrowmere HM1 7BD</div>
  </div>
</section>

<section class="featured">
  <div class="wrap">
    <div class="featured-head">
      <h2>Featured Products</h2>
      <div class="arrows">
        <span class="arrow-btn"><svg width="8" height="12" viewBox="0 0 8 12"><path d="M6 1L1 6l5 5" stroke="#666" stroke-width="2" fill="none"/></svg></span>
        <span class="arrow-btn"><svg width="8" height="12" viewBox="0 0 8 12"><path d="M2 1l5 5-5 5" stroke="#666" stroke-width="2" fill="none"/></svg></span>
      </div>
    </div>
    <div class="product-row">
      <div class="product"><div class="product-photo" role="img" aria-label="Black smartphone front view"></div><div class="product-name">Screen Replacement</div><div class="product-buy"><span class="price">£50.00</span><span class="cart-btn"><svg width="14" height="14" viewBox="0 0 24 24"><path d="M2 3h4l3 12h11l2-8H7" stroke="#fff" stroke-width="2.5" fill="none"/><circle cx="10" cy="20" r="2" fill="#fff"/><circle cx="18" cy="20" r="2" fill="#fff"/></svg></span></div></div>
      <div class="product"><div class="product-photo" role="img" aria-label="Silver and white smartphones" style="background:linear-gradient(160deg,#d9d9d9,#8e8e8e)"></div><div class="product-name">Screen Replacement</div><div class="product-buy"><span class="price">£50.00</span><span class="cart-btn"><svg width="14" height="14" viewBox="0 0 24 24"><path d="M2 3h4l3 12h11l2-8H7" stroke="#fff" stroke-width="2.5" fill="none"/><circle cx="10" cy="20" r="2" fill="#fff"/><circle cx="18" cy="20" r="2" fill="#fff"/></svg></span></div></div>
      <div class="product"><div class="product-photo" role="img" aria-label="Black smartphone front view"></div><div class="product-name">Screen Replacement</div><div class="product-buy"><span class="price">£50.00</span><span class="cart-btn"><svg width="14" height="14" viewBox="0 0 24 24"><path d="M2 3h4l3 12h11l2-8H7" stroke="#fff" stroke-width="2.5" fill="none"/><circle cx="10" cy="20" r="2" fill="#fff"/><circle cx="18" cy="20" r="2" fill="#fff"/></svg></span></div></div>
      <div class="product"><div class="product-photo" role="img" aria-label="Smartphone shown from front and side" style="background:linear-gradient(160deg,#444,#9a9a9a)"></div><div class="product-name">Screen Replacement</div><div class="product-buy"><span class="price">£50.00</span><span class="cart-btn"><svg width="14" height="14" viewBox="0 0 24 24"><path d="M2 3h4l3 12h11l2-8H7" stroke="#fff" stroke-width="2.5" fill="none"/><circle cx="10" cy="20" r="2" fill="#fff"/><circle cx="18" cy="20" r="2" fill="#fff"/></svg></span></div></div>
      <div class="product"><div class="product-photo" role="img" aria-label="Smartphone with glass screen protector" style="background:linear-gradient(160deg,#3a4a5c,#c6d2dc)"></div><div class="product-name">Screen Replacement</div><div class="product-buy"><span class="price">£50.00</span><span class="cart-btn"><svg width="14" height="14" viewBox="0 0 24 24"><path d="M2 3h4l3 12h11l2-8H7" stroke="#fff" stroke-width="2.5" fill="none"/><circle cx="10" cy="20" r="2" fill="#fff"/><circle cx="18" cy="20" r="2" fill="#fff"/></svg></span></div></div>
    </div>
  </div>
</section>

<section class="steps">
  <div class="wrap">
    <h2>Get Your Mobile Phone Repaired In Just Four Easy Steps</h2>
    <div class="step-row">
      <div class="step-card"><div class="step-head">Pay Online</div><div class="step-icon"><svg width="36" height="36" viewBox="0 0 24 24"><rect x="4" y="7" width="16" height="12" rx="1" fill="none" stroke="#0592cd" stroke-width="2"/><path d="M8 7V5h8v2M9 13l2 2 4-4" stroke="#0592cd" stroke-width="2" fill="none"/></svg></div><div class="step-num">Step 1</div><p class="step-text">Choose your device and repair, then pay securely online in a few clicks.</p><div class="step-more">Read More</div></div>
      <div class="step-card"><div class="step-head">Print Invoice</div><div class="step-icon"><svg width="36" height="36" viewBox="0 0 24 24"><rect x="3" y="9" width="18" height="8" rx="1" fill="none" stroke="#0592cd" stroke-width="2"/><path d="M7 9V3h10v6M7 14h10v7H7z" stroke="#0592cd" stroke-width="2" fill="none"/></svg></div><div class="step-num">Step 2</div><p class="step-text">Print the invoice we email you and pack it safely with your device.</p><div class="step-more">Read More</div></div>
      <div class="step-card"><div class="step-head">Send By Post</div><div class="step-icon"><svg width="36" height="36" viewBox="0 0 24 24"><path d="M3 8l9-5 9 5v9l-9 5-9-5z M3 8l9 5 9-5 M12 13v9" stroke="#0592cd" stroke-width="2" fill="none"/></svg></div><div class="step-num">Step 3</div><p class="step-text">Post it to us free of charge using our prepaid FreePost address label.</p><div class="step-more">Read More</div></div>
      <div class="step-card"><div class="step-head">Receive Back</div><div class="step-icon"><svg width="36" height="36" viewBox="0 0 24 24"><path d="M3 12a9 9 0 0115-6.7L21 8M21 3v5h-5M21 12a9 9 0 01-15 6.7L3 16M3 21v-5h5" stroke="#0592cd" stroke-width="2" fill="none"/></svg></div><div class="step-num">Step 4</div><p class="step-text">We repair and test it, then return it to your door the very same day.</p><div class="step-more">Read More</div></div>
    </div>
  </div>
</section>

<section class="benefits">
  <div class="wrap">
    <div class="col">
      <h3>Benefits of why to use our Services</h3>
      <div class="benefit"><span class="diamond"></span><div><div class="benefit-title">Nationwide Repair Service</div><p class="benefit-text">Wherever you are in the country, send your device to us and we will fix it fast.</p></div></div>
      <div class="benefit"><span class="diamond"></span><div><div class="benefit-title">Fast Service Free Return Delivery</div><p class="benefit-text">Most repairs finished on arrival, with tracked delivery back at no extra cost.</p></div></div>
      <div class="benefit"><span class="diamond"></span><div><div class="benefit-title">Excellent UK Based Customer Service</div><p class="benefit-text">Our friendly local team is on hand to answer every question you may have.</p></div></div>
    </div>
    <div class="col">
      <h3>Same Day Repairs Instore</h3>
      <div class="instore-media">
        <div class="instore-photo" role="img" aria-label="Technician repairing a phone in the store"></div>
        <p class="small-text">Visit one of our stores and have your phone or tablet repaired while you wait. Most screen and battery jobs are done within the hour by trained staff.</p>
      </div>
      <p class="small-text" style="margin-top:14px">Unit 12, Fernbrook Retail Park, Harrowmere HM4 2QT. Open Monday to Saturday, no appointment needed.</p>
    </div>
  </div>
</section>

<section class="testimonial">
  <div class="wrap">
    <div class="avatar" role="img" aria-label="Portrait of a happy customer"></div>
    <div>
      <div class="quote-mark">“</div>
      <p class="quote-text">I sent my cracked phone on Monday morning and it was back with me by Tuesday, looking brand new. The team kept me updated the whole way and the price was exactly as quoted online. I would not hesitate to use them again for any repair.</p>
    </div>
  </div>
  <div class="dots"><span></span><span class="on"></span><span></span></div>
</section>

<section class="cta-bar">
  <div class="wrap">
    <div class="cta-phone"><svg width="22" height="22" viewBox="0 0 24 24"><path d="M6 2l4 4-2 3c1 3 4 6 7 7l3-2 4 4-3 4C10 22 2 14 2 5z" fill="#555"/></svg>01632 960418</div>
    <div class="cta-main">
      <svg width="18" height="12" viewBox="0 0 18 12"><path d="M0 6h16M11 1l5 5-5 5" stroke="#acd036" stroke-width="2" fill="none"/></svg>
      Get Your Device Repaired Online Today
      <svg width="18" height="12" viewBox="0 0 18 12"><path d="M18 6H2M7 1L2 6l5 5" stroke="#acd036" stroke-width="2" fill="none"/></svg>
    </div>
    <div class="socials"><span></span><span></span><span></span><span></span></div>
  </div>
</section>

<section class="partners">
  <div class="wrap">
    <svg width="14" height="24" viewBox="0 0 14 24"><path d="M12 2L2 12l10 10" stroke="#aaa" stroke-width="3" fill="none"/></svg>
    <div class="partner"><span></span></div>
    <div class="partner"><span></span></div>
    <div class="partner"><span></span></div>
    <div class="partner"><span></span></div>
    <div class="partner"><span></span></div>
    <div class="partner"><span></span></div>
    <div class="partner"><span></span></div>
    <svg width="14" height="24" viewBox="0 0 14 24"><path d="M2 2l10 10-10 10" stroke="#aaa" stroke-width="3" fill="none"/></svg>
  </div>
</section>

<footer class="site-footer">
  <div class="wrap">
    <div class="f-col">
      <h4>Newsletter</h4>
      <div class="field">Name</div>
      <div class="field">Email Address</div>
      <span class="btn-submit">Submit</span>
    </div>
    <div class="f-col">
      <h4>Contact us</h4>
      <p class="f-text">Unit 12, Fernbrook Retail Park<br>Harrowmere HM4 2QT<br>Tel: 01632 960418<br>www.tallowcrestdesk.co.uk</p>
      <div class="f-socials"><span></span><span></span><span></span></div>
    </div>
    <div class="f-col">
      <h4>Pearphone Repairs</h4>
      <ul class="f-list"><li>Pearphone 4 Repairs</li><li>Pearphone 4S Repairs</li><li>Pearphone 5 Repairs</li><li>Pearphone 5C Repairs</li><li>Pearpad Repairs</li></ul>
    </div>
    <div class="f-col">
      <h4>Samvo Repairs</h4>
      <ul class="f-list"><li>Stellar S3 Repairs</li><li>Stellar S4 Repairs</li><li>Stellar Note 3</li><li>Stellar S5 Repairs</li><li>Stellar Tab Repairs</li></ul>
    </div>
  </div>
</footer>
<div class="copyright">Copyright Tallowcrest Desk 2015. All Rights Reserved. Terms &amp; Privacy</div>

</body>
</html>
```